Bruntel general construction

We need an website that are similar to these websites:
https://www.morvexa.com/en/
https://dulnari.com/company/

but with a tweak. Do not copy the entire website but atleast similar and yet better than them.

For reference this our current website.
https://bruntel.ph/

For the winning Designer please help us with the migration from our old website to the new redesign website.

```html
<!DOCTYPE html>
<html lang="en">
<head>
<meta charset="utf-8">
<title>Bruntel — Industrial Services Group</title>
<link href="https://fonts.googleapis.com/css2?family=Manrope:wght@500;600;700;800&family=Inter:wght@400;500;600;700&display=swap" rel="stylesheet">
<style>
:root{
  --orange:#f26a21;
  --orange-dark:#e05a14;
  --navy:#0f1b2d;
  --navy-2:#16243a;
  --ink:#0f1726;
  --muted:#5d6675;
  --line:#e3e6eb;
  --light:#f4f6f9;
  --white:#ffffff;
}
*{box-sizing:border-box;margin:0;padding:0}
html,body{width:1200px;height:4494px;overflow:hidden}
body{font-family:"Inter",sans-serif;color:var(--ink);background:var(--white);position:relative}
h1,h2,h3,.display{font-family:"Manrope",sans-serif;letter-spacing:-0.02em}
.accent{color:var(--orange)}
.eyebrow{font-size:10px;font-weight:600;color:var(--orange);margin-bottom:8px}
.btn{display:inline-flex;align-items:center;justify-content:space-between;gap:14px;font-size:11px;font-weight:700;padding:0 20px;height:40px;text-decoration:none}
.btn svg{width:12px;height:12px}
.btn-orange{background:var(--orange);color:#fff}
.btn-outline-light{border:1px solid rgba(255,255,255,.5);color:#fff}
.btn-outline-dark{border:1.5px solid var(--ink);color:var(--ink)}
.btn-dark{background:var(--ink);color:#fff}

/* hero */
.hero{position:absolute;left:0;top:0;width:1200px;height:735px}
.hero-media{position:absolute;inset:0 0 0 0;height:700px;background:linear-gradient(90deg,rgba(14,22,34,.92) 0%,rgba(20,28,40,.75) 45%,rgba(60,50,45,.55) 100%),linear-gradient(180deg,#3c4654 0%,#2a2f37 55%,#3a2f29 100%)}
.nav{position:absolute;top:26px;left:91px;right:91px;height:32px;display:flex;align-items:center}
.logo{display:flex;align-items:center;gap:8px;font-family:"Manrope",sans-serif;font-weight:800;font-size:16px;color:#fff}
.logo-box{width:28px;height:28px;background:var(--orange);border-radius:4px}
.nav-links{display:flex;gap:0;margin-left:124px;list-style:none}
.nav-links li{font-size:11px;color:#dfe3ea;margin-right:56px;padding-bottom:4px}
.nav-links li.active{color:var(--orange);border-bottom:2px solid var(--orange)}
.nav-phone{margin-left:auto;font-size:11px;color:#dfe3ea;display:flex;gap:6px;align-items:center}
.nav-phone svg{width:12px;height:12px}
.nav-cta{margin-left:18px;height:32px;padding:0 24px;font-size:11px}
.hero-content{position:absolute;left:91px;top:190px;width:560px}
.hero h1{font-size:62px;line-height:1;color:#fff;font-weight:800;margin:6px 0 28px;width:820px}
.hero p{font-size:15px;line-height:1.6;color:#e6e9ee;width:520px}
.hero-actions{display:flex;gap:9px;margin-top:20px}
.hero-actions .btn:first-child{width:219px}
.hero-actions .btn:last-child{width:166px}
.stats{position:absolute;left:45px;top:617px;width:1110px;height:118px;background:var(--orange);display:grid;grid-template-columns:repeat(4,1fr);padding-left:100px;align-items:center}
.stat strong{display:block;font-family:"Manrope",sans-serif;font-size:40px;font-weight:800;color:#fff;line-height:1}
.stat span{font-size:11px;color:#fff;display:block;margin-top:10px}

/* about */
.about{position:absolute;top:735px;left:0;width:1200px;height:625px}
.about-media{position:absolute;left:82px;top:123px;width:502px;height:377px;background:linear-gradient(160deg,#b9a48a 0%,#8e7e6c 40%,#6a5a4c 100%)}
.about-badge{position:absolute;left:459px;top:433px;width:144px;height:88px;background:var(--orange);color:#fff;padding:16px 18px}
.about-badge strong{font-family:"Manrope",sans-serif;font-size:28px;font-weight:800;display:block;line-height:1}
.about-badge span{font-size:10px;display:block;margin-top:8px}
.about-text{position:absolute;left:637px;top:98px;width:480px}
.about-text h2{font-size:40px;line-height:1.05;font-weight:800;margin-bottom:22px}
.about-text p{font-size:15px;line-height:1.55;color:var(--muted)}
.checks{list-style:none;margin-top:24px}
.checks li{display:flex;align-items:center;gap:12px;font-size:13px;margin-bottom:15px}
.tick{width:19px;height:19px;background:var(--ink);display:flex;align-items:center;justify-content:center}
.tick svg{width:11px;height:11px}
.about-text .btn{margin-top:20px;width:212px;height:38px}

/* services */
.services{position:absolute;top:1360px;left:0;width:1200px;height:1120px;background:var(--light)}
.section-head{position:absolute;left:72px;top:103px;width:1056px}
.section-head h2{font-size:40px;line-height:1.05;font-weight:800}
.section-head p{font-size:15px;color:var(--muted);line-height:1.55;width:610px;margin-top:16px}
.section-head .btn{position:absolute;right:0;top:128px;width:158px}
.grid{position:absolute;left:72px;display:grid;grid-template-columns:repeat(3,338px);gap:21px}
.services .grid{top:311px;row-gap:22px}
.card{background:#fff;border:1px solid var(--line);height:356px;position:relative}
.card-media{height:172px;position:relative}
.card-icon{position:absolute;left:16px;top:12px;width:36px;height:36px;background:var(--orange);display:flex;align-items:center;justify-content:center}
.card-icon svg{width:16px;height:16px}
.card-body{padding:22px 20px}
.card h3{font-size:16px;font-weight:700;margin-bottom:14px}
.card p{font-size:11px;line-height:1.75;color:var(--muted)}
.card .more{position:absolute;left:20px;bottom:26px;font-size:11px;font-weight:600;color:var(--orange);display:flex;gap:42px}
.m1{background:linear-gradient(135deg,#7a8590,#4d5660)}
.m2{background:linear-gradient(180deg,#7d93ad,#4f5a66)}
.m3{background:linear-gradient(135deg,#9aa3aa,#c6c9cc 60%,#6b7277)}
.m4{background:linear-gradient(135deg,#546372,#8a4b30 60%,#3d4650)}
.m5{background:linear-gradient(135deg,#6f6a63,#a88a66 55%,#3f3c39)}
.m6{background:linear-gradient(180deg,#5f7488,#56684d 55%,#7a8f8c)}

/* principles */
.principles{position:absolute;top:2480px;left:0;width:1200px;height:551px;background:var(--navy);text-align:center}
.principles .eyebrow{margin-top:85px}
.principles h2{font-size:40px;color:#fff;font-weight:800}
.principles .sub{font-size:15px;color:#aab3c0;margin-top:18px}
.principles .grid{top:232px}
.pcard{background:var(--navy-2);border:1px solid #26344a;height:211px;text-align:left;padding:28px 27px}
.pcard .card-icon{position:static;width:46px;height:46px;margin-bottom:22px}
.pcard h3{color:#fff;font-size:16px;font-weight:700;margin-bottom:14px}
.pcard p{font-size:11px;line-height:1.75;color:#8590a0}

/* projects */
.projects{position:absolute;top:3031px;left:0;width:1200px;height:612px}
.projects .section-head{top:102px}
.projects .section-head .btn{top:24px;right:7px;width:155px;height:43px}
.projects .grid{top:246px}
.pcase{height:265px;position:relative;color:#fff}
.pcase-info{position:absolute;left:20px;bottom:22px}
.pcase-info small{font-size:9px;color:var(--orange);display:block;margin-bottom:6px}
.pcase-info h3{font-size:16px;font-weight:700;margin-bottom:10px}
.pcase-info span{font-size:11px;font-weight:600}
.pc1{background:linear-gradient(180deg,#6f8596 0%,#4f6657 55%,#0f1726 100%)}
.pc2{background:linear-gradient(180deg,#7a6f62 0%,#5d4b3d 55%,#0f1726 100%)}
.pc3{background:linear-gradient(180deg,#4a4d52 0%,#2e3034 55%,#0f1726 100%)}

/* cta */
.cta{position:absolute;top:3643px;left:134px;width:932px;height:262px;background:var(--orange);text-align:center;color:#fff}
.cta h2{font-size:30px;font-weight:800;margin-top:60px}
.cta p{font-size:13px;line-height:1.6;width:520px;margin:14px auto 0}
.cta-actions{display:flex;justify-content:center;gap:9px;margin-top:14px}
.cta-actions .btn:first-child{width:183px;height:38px}
.cta-actions .btn:last-child{width:138px;height:38px;border:1px solid rgba(255,255,255,.7);color:#fff}

/* footer */
.footer{position:absolute;top:4004px;left:0;width:1200px;height:490px;background:var(--navy);color:#aab3c0}
.footer-col{position:absolute;top:110px}
.footer-col h4{font-size:10px;color:var(--orange);font-weight:600;margin-bottom:18px}
.footer-col ul{list-style:none}
.footer-col li{font-size:12px;margin-bottom:15px;color:#aab3c0}
.footer-brand{left:72px;top:104px;width:320px}
.footer-brand .logo{margin-bottom:20px}
.footer-brand p{font-size:11px;line-height:1.75}
.socials{display:flex;gap:12px;margin-top:24px}
.socials span{width:30px;height:30px;border:1px solid #3a4658}
.contact li{display:flex;gap:12px;font-size:11px;line-height:1.5;width:240px}
.contact svg{width:13px;height:13px;flex:none;margin-top:2px}
.contact .quote{color:var(--orange);font-weight:600;gap:60px}
.footer-bottom{position:absolute;left:72px;right:72px;top:375px;border-top:1px solid #223048;padding-top:8px;display:flex;font-size:10px;color:#6f7b8c}
.footer-bottom nav{margin-left:auto;display:flex;gap:20px}
</style>
</head>
<body>

<header class="hero">
  <div class="hero-media" role="img" aria-label="Industrial refinery plant at dusk with pipes and towers"></div>
  <nav class="nav">
    <div class="logo"><span class="logo-box"></span>BRUNTEL</div>
    <ul class="nav-links">
      <li class="active">Home</li><li>About</li><li>Services</li><li>Projects</li><li>News</li><li>Careers</li>
    </ul>
    <div class="nav-phone"><svg viewBox="0 0 24 24" fill="none" stroke="#f26a21" stroke-width="2"><path d="M5 3h4l2 5-3 2a11 11 0 0 0 6 6l2-3 5 2v4a2 2 0 0 1-2 2A17 17 0 0 1 3 5a2 2 0 0 1 2-2z"/></svg>+63 (0) 917-000-4821</div>
    <a class="btn btn-orange nav-cta">Contact Us</a>
  </nav>
  <div class="hero-content">
    <div class="eyebrow">Industrial Services Group</div>
    <h1>Building, protecting and maintaining industry.</h1>
    <p>BRUNTEL is a multi-discipline industrial services group insulation, scaffolding, coatings, mechanical and maintenance trusted by world-renowned EPC contractors to deliver safely and to the highest standard.</p>
    <div class="hero-actions">
      <a class="btn btn-orange">Explore our services<svg viewBox="0 0 24 24" fill="none" stroke="#fff" stroke-width="2.5"><path d="M4 12h16M14 6l6 6-6 6"/></svg></a>
      <a class="btn btn-outline-light">Talk to our team</a>
    </div>
  </div>
  <div class="stats">
    <div class="stat"><strong>25+</strong><span>Years of operation</span></div>
    <div class="stat"><strong>1,200+</strong><span>Projects delivered</span></div>
    <div class="stat"><strong>3,500+</strong><span>Skilled personnel</span></div>
    <div class="stat"><strong>12</strong><span>Countries served</span></div>
  </div>
</header>

<section class="about">
  <div class="about-media" role="img" aria-label="Construction crew in orange coveralls reviewing a tablet on site with cranes behind"></div>
  <div class="about-badge"><strong>25+</strong><span>Years delivering</span></div>
  <div class="about-text">
    <div class="eyebrow">Who we are</div>
    <h2>One partner for the full <span class="accent">industrial lifecycle</span></h2>
    <p>From construction and installation through protection and maintenance, BRUNTEL brings the trades that keep plants running under one roof. What began as specialist support to environmental EPC contractors has grown into a full multi-discipline industrial services group.</p>
    <ul class="checks">
      <li><span class="tick"><svg viewBox="0 0 24 24" fill="none" stroke="#fff" stroke-width="3"><path d="M5 12l5 5 9-10"/></svg></span>A single accountable partner across multiple disciplines</li>
      <li><span class="tick"><svg viewBox="0 0 24 24" fill="none" stroke="#fff" stroke-width="3"><path d="M5 12l5 5 9-10"/></svg></span>Certified crews and international HSE standards</li>
      <li><span class="tick"><svg viewBox="0 0 24 24" fill="none" stroke="#fff" stroke-width="3"><path d="M5 12l5 5 9-10"/></svg></span>Rooted in environmental EPC delivery</li>
    </ul>
    <a class="btn btn-outline-dark">More about BRUNTEL<svg viewBox="0 0 24 24" fill="none" stroke="#0f1726" stroke-width="2.5"><path d="M4 12h16M14 6l6 6-6 6"/></svg></a>
  </div>
</section>

<section class="services">
  <div class="section-head">
    <div class="eyebrow">What we do</div>
    <h2>Multi-discipline services,<br><span class="accent">single accountability</span></h2>
    <p>Six core disciplines that cover the industrial asset lifecycle deployed individually or as fully integrated site teams.</p>
    <a class="btn btn-orange" style="justify-content:center">All services<svg viewBox="0 0 24 24" fill="none" stroke="#fff" stroke-width="2.5"><path d="M4 12h16M14 6l6 6-6 6"/></svg></a>
  </div>
  <div class="grid">
    <article class="card"><div class="card-media m1" role="img" aria-label="Worker wrapping insulation on process piping"><span class="card-icon"><svg viewBox="0 0 24 24" fill="none" stroke="#fff" stroke-width="2"><path d="M12 3l9 5-9 5-9-5 9-5zM3 13l9 5 9-5"/></svg></span></div><div class="card-body"><h3>Thermal Insulation</h3><p>Complete thermal, acoustic and fire-protection insulation systems for process plants, power generation and marine assets engineered to cut energy loss and keep operations compliant.</p></div><div class="more">Learn more<span>↗</span></div></article>
    <article class="card"><div class="card-media m2" role="img" aria-label="Steel scaffolding around an industrial structure"><span class="card-icon"><svg viewBox="0 0 24 24" fill="none" stroke="#fff" stroke-width="2"><path d="M4 4v16M20 4v16M4 9h16M4 15h16"/></svg></span></div><div class="card-body"><h3>Scaffolding &amp; Access</h3><p>Design, erection and dismantling of scaffolding and specialist access systems that keep every worksite productive and your teams protected at height.</p></div><div class="more">Learn more<span>↗</span></div></article>
    <article class="card"><div class="card-media m3" role="img" aria-label="Worker in protective suit spray coating a tank wall"><span class="card-icon"><svg viewBox="0 0 24 24" fill="none" stroke="#fff" stroke-width="2"><rect x="5" y="8" width="10" height="12"/><path d="M8 8V4h4v4M15 11h4"/></svg></span></div><div class="card-body"><h3>Surface Protection &amp; Coatings</h3><p>Blasting, protective coatings and passive fire protection that extend asset life and defend structures against corrosion, chemicals and extreme environments.</p></div><div class="more">Learn more<span>↗</span></div></article>
    <article class="card"><div class="card-media m4" role="img" aria-label="Technicians working on a pump and piping assembly"><span class="card-icon"><svg viewBox="0 0 24 24" fill="none" stroke="#fff" stroke-width="2"><path d="M14 6a4 4 0 0 0 5 5l-9 9-4-4 9-9a4 4 0 0 1-1-1z"/></svg></span></div><div class="card-body"><h3>Mechanical &amp; Piping</h3><p>Fabrication, installation and commissioning of piping, static and rotating equipment delivered by certified crews to exacting quality and safety standards.</p></div><div class="more">Learn more<span>↗</span></div></article>
    <article class="card"><div class="card-media m5" role="img" aria-label="Maintenance crew inside a plant during turnaround"><span class="card-icon"><svg viewBox="0 0 24 24" fill="none" stroke="#fff" stroke-width="2"><path d="M12 3l8 3v6c0 5-4 8-8 9-4-1-8-4-8-9V6z"/></svg></span></div><div class="card-body"><h3>Plant Maintenance &amp; Turnarounds</h3><p>Integrated maintenance, shutdown and turnaround management that keeps plants running safely planned, resourced and executed to bring assets back online on schedule.</p></div><div class="more">Learn more<span>↗</span></div></article>
    <article class="card"><div class="card-media m6" role="img" aria-label="Aerial view of a wastewater treatment plant"><span class="card-icon"><svg viewBox="0 0 24 24" fill="none" stroke="#fff" stroke-width="2"><path d="M4 12a8 8 0 0 1 14-5M20 12a8 8 0 0 1-14 5M18 3v4h-4M6 21v-4h4"/></svg></span></div><div class="card-body"><h3>Environmental EPC Support</h3><p>Our roots. Specialist construction and mechanical support to world-renowned environmental EPC contractors from water and wastewater treatment plants to resource-recovery facilities.</p></div><div class="more">Learn more<span>↗</span></div></article>
  </div>
</section>

<section class="principles">
  <div class="eyebrow">How we work</div>
  <h2>Principles behind every project</h2>
  <p class="sub">Three commitments guide how we operate on every site, for every client.</p>
  <div class="grid">
    <div class="pcard"><span class="card-icon"><svg viewBox="0 0 24 24" fill="none" stroke="#fff" stroke-width="2"><path d="M12 3l8 3v6c0 5-4 8-8 9-4-1-8-4-8-9V6z"/><path d="M9 12l2 2 4-4"/></svg></span><h3>Safety First, Always</h3><p>An uncompromising HSE culture protects our people, clients and communities on every site, every day.</p></div>
    <div class="pcard"><span class="card-icon"><svg viewBox="0 0 24 24" fill="none" stroke="#fff" stroke-width="2"><path d="M4 17h16M6 17a6 6 0 0 1 12 0M12 8v3"/></svg></span><h3>Skilled, Certified People</h3><p>A multi-disciplinary workforce trained and certified to international standards forms the backbone of our delivery.</p></div>
    <div class="pcard"><span class="card-icon"><svg viewBox="0 0 24 24" fill="none" stroke="#fff" stroke-width="2"><path d="M12 3c4 4 6 7 6 11a6 6 0 0 1-12 0c0-3 2-5 3-6 0 3 2 4 3 4-1-3 0-6 0-9z"/></svg></span><h3>Environmental Responsibility</h3><p>Rooted in environmental EPC work, we help clients operate cleaner, more efficient and more sustainable assets.</p></div>
  </div>
</section>

<section class="projects">
  <div class="section-head">
    <div class="eyebrow">Selected work</div>
    <h2>Projects that speak for us</h2>
    <p style="margin-top:10px">A snapshot of recent delivery across water, power and oil &amp; gas.</p>
    <a class="btn btn-dark" style="justify-content:center">All projects<svg viewBox="0 0 24 24" fill="none" stroke="#fff" stroke-width="2.5"><path d="M4 12h16M14 6l6 6-6 6"/></svg></a>
  </div>
  <div class="grid">
    <article class="pcase pc1" role="img" aria-label="Aerial view of a water reclamation facility"><div class="pcase-info"><small>Water · 2024</small><h3>Coastal Water Reclamation Facility</h3><span>View project ↗</span></div></article>
    <article class="pcase pc2" role="img" aria-label="Refinery interior with workers during turnaround"><div class="pcase-info"><small>Oil &amp; Gas · 2023</small><h3>Refinery Major Turnaround</h3><span>View project ↗</span></div></article>
    <article class="pcase pc3" role="img" aria-label="Power plant structure under a cloudy sky"><div class="pcase-info"><small>Power · 2023</small><h3>Power Plant Insulation Upgrade</h3><span>View project ↗</span></div></article>
  </div>
</section>

<section class="cta">
  <h2>Ready to build something that lasts?</h2>
  <p>Talk to our team about your next project. From a single scope to a full turnaround, BRUNTEL delivers safely, on quality and on time.</p>
  <div class="cta-actions">
    <a class="btn btn-dark">Request a quote<svg viewBox="0 0 24 24" fill="none" stroke="#fff" stroke-width="2.5"><path d="M4 12h16M14 6l6 6-6 6"/></svg></a>
    <a class="btn">Our services</a>
  </div>
</section>

<footer class="footer">
  <div class="footer-col footer-brand">
    <div class="logo"><span class="logo-box"></span>BRUNTEL</div>
    <p>A multi-discipline industrial services group delivering insulation, access, coatings, mechanical and maintenance solutions built on a foundation of environmental EPC expertise.</p>
    <div class="socials"><span></span><span></span></div>
  </div>
  <div class="footer-col" style="left:436px"><h4>Services</h4><ul><li>Thermal Insulation</li><li>Scaffolding &amp; Access</li><li>Surface Protection &amp; Coatings</li><li>Mechanical &amp; Piping</li><li>Plant Maintenance &amp; Turnarounds</li><li>Environmental EPC Support</li></ul></div>
  <div class="footer-col" style="left:710px"><h4>Company</h4><ul><li>About Us</li><li>Projects</li><li>News &amp; Media</li><li>Careers</li><li>Contact</li></ul></div>
  <div class="footer-col contact" style="left:893px"><h4>Get in touch</h4><ul>
    <li><svg viewBox="0 0 24 24" fill="none" stroke="#f26a21" stroke-width="2"><path d="M12 21s7-6 7-12a7 7 0 0 0-14 0c0 6 7 12 7 12z"/><circle cx="12" cy="9" r="2.5"/></svg>14 Kalinaw Street, Brgy. Maliwanag, Lumbang City, Cavite Philippines 4120</li>
    <li><svg viewBox="0 0 24 24" fill="none" stroke="#f26a21" stroke-width="2"><path d="M5 3h4l2 5-3 2a11 11 0 0 0 6 6l2-3 5 2v4a2 2 0 0 1-2 2A17 17 0 0 1 3 5a2 2 0 0 1 2-2z"/></svg>+63 (0) 917-000-4821</li>
    <li><svg viewBox="0 0 24 24" fill="none" stroke="#f26a21" stroke-width="2"><rect x="3" y="5" width="18" height="14"/><path d="M3 6l9 7 9-7"/></svg>info@bruntel.ph</li>
    <li class="quote">Request a quote<span>↗</span></li>
  </ul></div>
  <div class="footer-bottom"><span>© 2026 BRUNTEL. All rights reserved.</span><nav><span>Privacy Policy</span><span>Terms of Use</span><span>HSE Policy</span></nav></div>
</footer>

</body>
</html>
```